Need Help Rebranding My Food Blog

I have a Wordpress Food blog called BeetBuddies.com. Right now it has no life and is very bland. I am rebranding this site to a new named called, TheHoneyedPath.com. I would love to have a blog that is vibrant and full of life and personality.

One of my top priorities when a new visitor comes to my site is to quickly understand what the site is about (Gluten-free, dairy-free sweets that taste delicious).

I also want people to feel a connection with me when they come to the site.

Here are some other things that I'd like in the blog design...

1. Optin
My business is driven by adding people to my list so it is very important for me to have an optin front and center/ above-the-fold. See https://www.clevertidyearnings.com/ as an example. The headline that I would like is "Gluten-free & dairy-free sweets that actually taste good"

2. Vibrant/full life
The next important aspect of this blog is that it is vibrant. I like colors that remind me of a SUNSET. See attachments for logo and color scheme. Here's an example of a site I really like that is vibrant: http://www.sugarandopendays.com/

Also see Image titled: "Sample: Feeling". Notice the feeling you get from the image/brush strokes and how it feels light, breezy, and free spirited.

3. Food Images
The last important aspect for my blog is to showcase my recipes. I have attached a few of them as examples. Its really important for a food blog to showcase beautiful pictures of recipes for people to see so will definitely need this in the design.

Also, attached...
1. Image of me.
2. New logo for TheHoneyedPath (notice: don't use the one attached as "Sample/Feeling". That's just for reference of the feeling I like.)

Thanks!

Marion

P.S. I didn't include all the copy that would be needed so feel free to use the "lorem ipsum" text as placeholder if need be.

Target Market(s)

stay-at-home moms, dairy-free & gluten allergies, love desserts & sweets

Coding

Coded - Design and coding required

Font styles to use
Sans Serif

Requirements
Must have
• 1. Optin area with my picture and what I'm about ""Gluten-free & dairy-free sweets that actually taste good""
• 2. Must have personality/vibrancy to the site. Think full of life, not dull like my current website... beetbuddies.com
• 3. Highlight food images (Vertical image holders only)
Nice to have
• Color scheme should be based on my logo
Should not have
• No black or grey colors

```html
<!DOCTYPE html>
<html lang="en">
<head>
<meta charset="utf-8">
<title>TheHoneyedPath — Gluten-free &amp; dairy-free sweets</title>
<link href="https://fonts.googleapis.com/css2?family=Roboto:wght@300;400;500;700&display=swap" rel="stylesheet">
<style>
:root{
  --coral:#f26b5b;
  --rose:#ee4d6d;
  --pink:#e8355f;
  --ink:#2b2b2b;
  --body:#5a5a5a;
  --line:#d9d6d6;
  --page:#f4f2f2;
  --card:#ffffff;
  --footer:#141414;
}
*{box-sizing:border-box;margin:0;padding:0}
html,body{width:1200px;height:4306px;overflow:hidden}
body{position:relative;background:var(--page);font-family:'Roboto',sans-serif;color:var(--body)}

/* header */
.site-header{position:absolute;top:0;left:0;width:1200px;height:123px;
  background:linear-gradient(90deg,var(--coral) 0%,#f57a6a 45%,var(--rose) 100%)}
.nav a{position:absolute;top:50px;color:#fff;text-decoration:none;font-size:16px;font-weight:500;letter-spacing:.3px}
.nav .active{font-weight:700}
.brand{position:absolute;top:34px;left:470px;width:260px;text-align:center;color:#fff;font-size:28px;font-weight:400;line-height:52px}

/* hero */
.hero{position:absolute;top:123px;left:0;width:1200px;height:408px;background:#e8e3de}
.hero-side{position:absolute;top:0;height:408px;width:34px}
.hero-side.left{left:0;background:linear-gradient(180deg,#c98a4a,#e6c38a)}
.hero-side.right{right:0;background:linear-gradient(180deg,#d2b06a,#b8782e)}
.hero-photo{position:absolute;top:0;left:34px;width:1132px;height:408px;
  background:radial-gradient(ellipse at 55% 55%,#f1a24c 0%,#d9742a 35%,#a5522a 60%,#6d4636 100%)}
.hero-caption{position:absolute;left:34px;bottom:0;width:1132px;height:78px;background:rgba(20,16,14,.72);text-align:center}
.hero-caption .kicker{display:block;margin-top:15px;color:var(--pink);font-size:14px}
.hero-caption h1{margin-top:5px;color:#fff;font-size:19px;font-weight:500}

/* optin */
.optin{position:absolute;top:585px;left:29px;width:1142px;height:62px;background:var(--card)}
.optin p{position:absolute;left:24px;top:20px;font-size:16px;color:var(--ink)}
.optin .field{position:absolute;top:13px;height:36px;border:1px solid var(--line);border-radius:18px;
  font-size:14px;color:var(--ink);padding:0 16px;line-height:34px;background:#fff}
.optin .name{left:502px;width:200px}
.optin .email{left:726px;width:220px}
.optin .btn{position:absolute;top:13px;left:970px;width:155px;height:36px;border-radius:18px;background:var(--pink);color:#fff;font-size:14px;font-weight:500;text-align:center;line-height:36px}

/* post cards */
.post{position:absolute;left:34px;width:1132px;background:var(--card);padding:32px 46px 0;
  display:flex;flex-direction:column;overflow:hidden}
.post h2{text-align:center;font-size:29px;font-weight:500;color:var(--ink);line-height:36px}
.tag-row{display:flex;align-items:center;justify-content:center;margin:8px 0 16px}
.tag-row::before,.tag-row::after{content:"";width:130px;height:1px;background:var(--line)}
.tag{background:var(--pink);color:#fff;font-size:11px;font-weight:500;padding:3px 22px;letter-spacing:.6px;text-transform:uppercase}
.photo{width:1040px}
.excerpt{margin-top:16px;font-size:14px;line-height:24px;color:var(--body)}
.more{align-self:center;margin-top:16px;border:1px solid #8a8a8a;color:var(--ink);font-size:13px;padding:7px 18px;text-transform:uppercase}
.post-meta{margin-top:auto;border-top:1px solid var(--line);height:72px;display:flex;align-items:center;font-size:13px;font-style:italic;color:var(--ink)}
.post-meta .item{display:flex;align-items:center;margin-right:22px}
.post-meta svg{margin-right:6px}
.share{margin-left:auto;display:flex;gap:8px}
.share span{width:26px;height:26px;border-radius:50%;border:1.5px solid #8a8a8a}
.share span.first{background:var(--pink);border-color:var(--pink)}

.ribbon{position:absolute;top:26px;left:-34px;width:150px;transform:rotate(-45deg);background:var(--pink);color:#fff;
  font-size:12px;text-align:center;line-height:24px}

.thumbs{position:relative;display:flex;width:1040px;height:184px}
.thumbs div{flex:1;height:184px}
.arrow{position:absolute;top:76px;width:26px;height:32px}
.arrow.prev{left:0;background:var(--pink)}
.arrow.next{right:0;background:var(--ink)}

/* pagination */
.pager{position:absolute;top:4131px;left:0;width:1200px;display:flex;justify-content:center;gap:10px}
.pager span{width:32px;height:32px;background:#fff;border:1px solid var(--line);font-size:14px;color:var(--ink);text-align:center;line-height:30px}
.pager .current{color:var(--pink)}

/* footer */
.site-footer{position:absolute;top:4210px;left:0;width:1200px;height:96px;background:var(--footer);text-align:center}
.footer-nav{margin-top:26px;font-size:14px;color:#cfcfcf}
.footer-nav a{color:#cfcfcf;text-decoration:none;margin:0 8px}
.footer-nav a.active{color:var(--pink)}
.copyright{margin-top:12px;font-size:13px;color:#bdbdbd}
.copyright b{color:var(--pink);font-weight:400}
</style>
</head>
<body>

<header class="site-header">
  <nav class="nav">
    <a class="active" style="left:200px">HOME</a>
    <a style="left:305px">ABOUT US</a>
    <a style="left:780px">RECIPES</a>
    <a style="left:900px">RESOURCES</a>
  </nav>
  <div class="brand">TheHoneyedPath</div>
</header>

<section class="hero">
  <div class="hero-side left" role="img" aria-label="Edge of previous slide: baked pastry photo"></div>
  <div class="hero-photo" role="img" aria-label="Bowl of creamy dairy-free soup with fresh herbs and bread"></div>
  <div class="hero-side right" role="img" aria-label="Edge of next slide: golden dessert photo"></div>
  <div class="hero-caption">
    <span class="kicker">Food and Lunch</span>
    <h1>Gluten-free &amp; dairy-free sweets that actually taste good"</h1>
  </div>
</section>

<form class="optin">
  <p>Subscribe to my newsletter to get updates in your inbox</p>
  <div class="field name">Your Name</div>
  <div class="field email">Your Email</div>
  <div class="btn">SUBSCRIBE NOW</div>
</form>

<article class="post" style="top:703px;height:884px">
  <div class="ribbon">Food of Week</div>
  <h2>Gluten-free &amp; Dairy-Free Mac n Cheese</h2>
  <div class="tag-row"><span class="tag">Dinner</span></div>
  <div class="photo" style="height:304px;background:linear-gradient(135deg,#e9a43a,#d4822a 50%,#f0bd5a)" role="img" aria-label="Close-up of gluten-free dairy-free macaroni and cheese"></div>
  <div class="thumbs">
    <div style="background:linear-gradient(135deg,#6a5a3a,#3e5a2a)" role="img" aria-label="Stir-fried vegetables thumbnail"></div>
    <div style="background:radial-gradient(circle,#e6a233,#c9c2b8)" role="img" aria-label="Bowl of orange sauce thumbnail"></div>
    <div style="background:linear-gradient(135deg,#e8e2d6,#c9bfae)" role="img" aria-label="Pasta shells thumbnail"></div>
    <div style="background:linear-gradient(135deg,#b0521e,#6a2a12)" role="img" aria-label="Roasted potatoes thumbnail"></div>
    <span class="arrow prev"></span><span class="arrow next"></span>
  </div>
  <p class="excerpt">Growing up, one of my all time favorite lunches had to be Macaroni n' Cheese. What's not to love? Pasta covered in mounds of cheese... can you really ever go wrong? Of course, growing up we ate the Cheddo box type; you know the powder stuff that was abnormally orange.Even as a child though, I knew that boxed Mac &amp; Cheese only tasted good when it was first made. Eating it reheated was another story.The cheese seemed to evaporate and the noodles would dry out so you were left with a dried non cheesy dust covering crispy</p>
  <span class="more">Continue Reading</span>
  <div class="post-meta">
    <span class="item"><svg width="12" height="12" viewBox="0 0 12 12"><circle cx="6" cy="4" r="3" fill="#e8355f"/><path d="M1 12a5 5 0 0 1 10 0z" fill="#e8355f"/></svg>Posted by: Marion</span>
    <span class="item"><svg width="14" height="12" viewBox="0 0 14 12"><path d="M1 1h12v7H6l-3 3V8H1z" fill="#e8355f"/></svg>Leave Comment</span>
    <div class="share"><span class="first"></span><span></span><span></span><span></span><span></span></div>
  </div>
</article>

<article class="post" style="top:1650px;height:804px">
  <h2>Dairy-Free Creamy Potato Soup</h2>
  <div class="tag-row"><span class="tag">Lunch</span></div>
  <div class="photo" style="height:382px;background:radial-gradient(ellipse at 45% 50%,#f6e7b8 0%,#f1dfae 35%,#f7f4ee 60%,#e9e6e0 100%)" role="img" aria-label="Bowl of creamy potato soup topped with bacon and green onions"></div>
  <p class="excerpt">This whipped potato soup actually makes you thankful for the brisk cold air. It's one of the best comfort foods. While I agree that some soup should be more broth and light this is NOT one of them.I am a firm believer that potato soup should be thick, smooth and hearty. Even without the dairy, this soup does not disappoint. In fact, my 4 year old just informed me that this is her favorite soup. Now, every time we have soup and it's not this dairy-free potato soup she gets extremely disappointed. "Mom, I really wanted the potato soup that's my favorite" she sadly states.</p>
  <span class="more">Continue Reading</span>
  <div class="post-meta">
    <span class="item"><svg width="12" height="12" viewBox="0 0 12 12"><circle cx="6" cy="4" r="3" fill="#e8355f"/><path d="M1 12a5 5 0 0 1 10 0z" fill="#e8355f"/></svg>Posted by: Marion</span>
    <span class="item"><svg width="14" height="12" viewBox="0 0 14 12"><path d="M1 1h12v7H6l-3 3V8H1z" fill="#e8355f"/></svg>Leave Comment</span>
    <div class="share"><span class="first"></span><span></span><span></span><span></span><span></span></div>
  </div>
</article>

<article class="post" style="top:2488px;height:778px">
  <h2>Cinnamon Swirl Popcorn</h2>
  <div class="tag-row"><span class="tag">Vegan</span></div>
  <div class="photo" style="height:385px;background:linear-gradient(135deg,#f3ece2,#e9d9c2 45%,#d9a47a 75%,#f4ede6)" role="img" aria-label="Bowl of cinnamon swirl popcorn"></div>
  <p class="excerpt">So, I have been making my own popcorn for a few years now.WHY? First, corn is a highly genetically modified food in our country and I want to make sure that if we eat corn it's organic. I'm sure there is microwavable organic popcorn somewhere but I have yet to see it on my store shelves. Secondly, I need our popcorn to be dairy-free.All that buttery goodness can't be enjoyed by this family without serious stomach issues. Lastly, like most packaged foods, companies just add extra ingredients for longer shelf life and...well, to make their food taste more like food. If you want to know more on what goes</p>
  <span class="more">Continue Reading</span>
  <div class="post-meta">
    <span class="item"><svg width="12" height="12" viewBox="0 0 12 12"><circle cx="6" cy="4" r="3" fill="#e8355f"/><path d="M1 12a5 5 0 0 1 10 0z" fill="#e8355f"/></svg>Posted by: Marion</span>
    <span class="item"><svg width="14" height="12" viewBox="0 0 14 12"><path d="M1 1h12v7H6l-3 3V8H1z" fill="#e8355f"/></svg>Leave Comment</span>
    <div class="share"><span class="first"></span><span></span><span></span><span></span><span></span></div>
  </div>
</article>

<article class="post" style="top:3315px;height:783px">
  <h2>Cinnamon Swirl Popcorn</h2>
  <div class="tag-row"><span class="tag">Vegan</span></div>
  <div class="photo" style="height:384px;background:radial-gradient(ellipse at 50% 45%,#f2b36a 0%,#eea257 40%,#f5f1ea 70%,#5a5a58 100%)" role="img" aria-label="White bowl of orange puree garnished with parsley"></div>
  <p class="excerpt">So, I have been making my own popcorn for a few years now.WHY? First, corn is a highly genetically modified food in our country and I want to make sure that if we eat corn it's organic. I'm sure there is microwavable organic popcorn somewhere but I have yet to see it on my store shelves. Secondly, I need our popcorn to be dairy-free.All that buttery goodness can't be enjoyed by this family without serious stomach issues. Lastly, like most packaged foods, companies just add extra ingredients for longer shelf life and...well, to make their food taste more like food. If you want to know more on what goes</p>
  <span class="more">Continue Reading</span>
  <div class="post-meta">
    <span class="item"><svg width="12" height="12" viewBox="0 0 12 12"><circle cx="6" cy="4" r="3" fill="#e8355f"/><path d="M1 12a5 5 0 0 1 10 0z" fill="#e8355f"/></svg>Posted by: Marion</span>
    <span class="item"><svg width="14" height="12" viewBox="0 0 14 12"><path d="M1 1h12v7H6l-3 3V8H1z" fill="#e8355f"/></svg>Leave Comment</span>
    <div class="share"><span class="first"></span><span></span><span></span><span></span><span></span></div>
  </div>
</article>

<nav class="pager">
  <span class="current">1</span><span>2</span><span>3</span><span>»</span>
</nav>

<footer class="site-footer">
  <div class="footer-nav">
    <a class="active">Home</a>/<a>About Us</a>/<a>Recipes</a>/<a>Resources</a>/<a>Contact Us</a>
  </div>
  <p class="copyright">Copyright © 2017 <b>TheHoneyedPath</b>. All rights reserved.</p>
</footer>

</body>
</html>
```